Looking for potential sellers

We help people buy and sell homes and are currently looking for potential home sellers. We offer low commissions, are the Local Colorado Springs and Falcon Experts, homes selling fast and at top dollar, Free expert pricing opinions and Consultations, over 9 years of experience, top rated Realtors creative and aggressive marketing strategies. Never merely own a house, THRIVE at Harborview. phone number 482-630-9157 web thriveatharborview.com

```html
<!DOCTYPE html>
<html lang="en">
<head>
<meta charset="utf-8">
<title>Cornerstone Real Estate Company – Postcard</title>
<link rel="stylesheet" href="https://fonts.googleapis.com/css2?family=Fira+Sans+Extra+Condensed:wght@300;400;500;600;700&display=swap">
<style>
  :root {
    --olive: #9c962f;
    --navy: #0f1b29;
    --white: #ffffff;
    --stage: #d2d2d2;
    --photo-light: #c9c9c9;
    --photo-mid: #8a7b70;
    --photo-dark: #3b4250;
    --stamp: #e5e5e5;
    --rule: #cfcfcf;
  }
  * { margin: 0; padding: 0; box-sizing: border-box; }
  html, body { width: 1200px; height: 735px; overflow: hidden; }
  body {
    background: var(--stage);
    display: flex;
    align-items: center;
    justify-content: center;
    gap: 20px;
    font-family: "Fira Sans Extra Condensed", "Arial Narrow", sans-serif;
  }
  .postcard { width: 570px; height: 380px; display: block; background: var(--white); }
  .fill-olive { fill: var(--olive); }
  .fill-navy { fill: var(--navy); }
  .fill-white { fill: var(--white); }
  .stroke-white { stroke: var(--white); fill: none; }
  .stroke-olive { stroke: var(--olive); fill: none; }
  .stroke-navy { stroke: var(--navy); fill: none; }
  text { font-family: "Fira Sans Extra Condensed", "Arial Narrow", sans-serif; }
  .headline { font-size: 48px; font-weight: 600; fill: var(--white); }
  .subline { font-size: 21px; font-weight: 300; fill: var(--white); }
  .subline b, .strong { font-weight: 600; }
  .slogan { font-size: 34px; font-weight: 500; fill: var(--white); }
  .tagline { font-size: 20px; font-weight: 600; fill: var(--white); }
  .web { font-size: 22px; font-weight: 400; fill: var(--navy); }
  .phone { font-size: 38px; font-weight: 600; fill: var(--olive); }
  .brand-name { font-weight: 500; fill: var(--navy); }
  .brand-sub { font-weight: 500; fill: var(--navy); letter-spacing: 0.5px; }
  .offer-title { font-size: 42px; fill: var(--white); }
  .offer-item { font-size: 15.5px; font-weight: 500; fill: var(--white); text-transform: uppercase; }
  .quote { font-size: 10.5px; font-weight: 400; fill: var(--white); }
  .quote-name { font-size: 12px; font-weight: 600; fill: var(--white); }
  .quote-role { font-size: 9.5px; font-style: italic; fill: var(--olive); }
  .quote-mark { font-size: 20px; font-weight: 700; fill: var(--olive); }
  .contact-lead { font-size: 19px; font-weight: 300; fill: var(--white); }
  .contact-phone { font-size: 22px; font-weight: 600; fill: var(--navy); }
  .side-url { font-size: 22px; font-weight: 400; fill: var(--white); }
</style>
</head>
<body>

<!-- Front of postcard -->
<svg class="postcard postcard-front" viewBox="0 0 652 435" xmlns="http://www.w3.org/2000/svg">
  <defs>
    <linearGradient id="portraitTone" x1="0" y1="0" x2="1" y2="1">
      <stop offset="0" stop-color="var(--photo-light)"/>
      <stop offset="0.55" stop-color="var(--photo-mid)"/>
      <stop offset="1" stop-color="var(--photo-dark)"/>
    </linearGradient>
  </defs>

  <polygon class="fill-olive accent-strip" points="0,22 210,22 218,40 0,40"/>

  <polygon class="portrait" role="img" aria-label="Portrait photo of the realtor, smiling, wearing a plaid shirt"
    fill="url(#portraitTone)" points="0,40 278,40 352,435 0,435"/>

  <polygon class="fill-navy divider-stripe" points="300,102 312,102 362,435 350,435"/>
  <polygon class="fill-navy header-block" points="314,105 398,105 404,135 322,135"/>
  <polygon class="fill-olive hero-panel" points="322,135 652,135 652,322 358,322"/>

  <g class="brand">
    <rect class="fill-olive" x="400" y="76" width="12" height="12"/>
    <text class="brand-name" x="420" y="94" font-size="38">cornerstone</text>
    <text class="brand-sub" x="628" y="128" font-size="10" text-anchor="end">REAL ESTATE COMPANY</text>
  </g>

  <text class="headline" x="368" y="205">It's Time...</text>
  <text class="subline" x="380" y="240">Never Merely <tspan class="strong">Own</tspan> a House,</text>
  <text class="slogan" x="630" y="281" text-anchor="end"><tspan class="strong">THRIVE</tspan> at Harborview.</text>

  <polygon class="fill-navy tagline-bar" points="338,322 652,322 652,352 343,352"/>
  <text class="tagline" x="342" y="345">We help people buy and sell homes .</text>

  <line class="stroke-olive" x1="322" y1="358" x2="652" y2="358" stroke-width="3"/>
  <line class="stroke-olive" x1="356" y1="428" x2="652" y2="428" stroke-width="3"/>

  <g class="icon-web stroke-navy" stroke-width="1.6">
    <circle cx="390" cy="376" r="10"/>
    <ellipse cx="390" cy="376" rx="4.5" ry="10"/>
    <line x1="380" y1="376" x2="400" y2="376"/>
    <line x1="382" y1="370" x2="398" y2="370"/>
    <line x1="382" y1="382" x2="398" y2="382"/>
  </g>
  <text class="web" x="410" y="384">www.thriveatharborview.com</text>

  <g class="icon-phone">
    <circle class="stroke-navy" cx="390" cy="406" r="11" stroke-width="1.6"/>
    <path class="fill-navy" d="M385,399 l3,-1 2,4 -2,2 q1,3 4,5 l2,-2 4,2 -1,3 q-8,0 -12,-13z"/>
  </g>
  <text class="phone" x="410" y="420">482-630-9157</text>
</svg>

<!-- Back of postcard -->
<svg class="postcard postcard-back" viewBox="0 0 652 435" xmlns="http://www.w3.org/2000/svg">
  <polygon class="fill-olive offer-panel" points="0,0 398,0 290,435 0,435"/>
  <polygon class="fill-navy edge-stripe" points="398,0 410,0 332,435 290,435"/>
  <polygon class="fill-navy edge-step" points="360,160 392,160 340,230 345,160"/>

  <text class="offer-title" x="14" y="53"><tspan font-weight="300">WE </tspan><tspan font-weight="600">OFFER</tspan></text>
  <rect class="fill-navy" x="170" y="45" width="158" height="9"/>

  <g class="offer-list">
    <g class="stroke-white" stroke-width="1.3">
      <rect x="18" y="70" width="10" height="10"/><path d="M20,75 l3,3 6,-8"/>
      <rect x="18" y="92" width="10" height="10"/><path d="M20,97 l3,3 6,-8"/>
      <rect x="18" y="114" width="10" height="10"/><path d="M20,119 l3,3 6,-8"/>
      <rect x="18" y="136" width="10" height="10"/><path d="M20,141 l3,3 6,-8"/>
      <rect x="18" y="158" width="10" height="10"/><path d="M20,163 l3,3 6,-8"/>
      <rect x="18" y="180" width="10" height="10"/><path d="M20,185 l3,3 6,-8"/>
    </g>
    <text class="offer-item" x="36" y="81">Low commissions,</text>
    <text class="offer-item" x="36" y="103">Local Colorado Springs and Falcon experts, homes</text>
    <text class="offer-item" x="36" y="125">Selling fast and at top dollar,</text>
    <text class="offer-item" x="36" y="147">Free expert pricing opinions and consultations,</text>
    <text class="offer-item" x="36" y="169">Over 9 years of experience,</text>
    <text class="offer-item" x="36" y="191">Top rated realtors creative and aggressive</text>
    <text class="offer-item" x="36" y="211">Marketing strategies.</text>
  </g>
  <circle class="fill-white" cx="289" cy="216" r="6"/>
  <circle class="fill-white" cx="305" cy="216" r="6"/>

  <polygon class="fill-navy testimonials" points="0,228 324,228 296,388 0,388"/>
  <g class="testimonial-frames stroke-white" stroke-width="0.8" opacity="0.7">
    <path d="M24,244 H12 V287 H116"/>
    <path d="M198,287 H262 L270,244 H292"/>
    <path d="M24,307 H12 V362 H112"/>
    <path d="M190,364 H250 L262,307 H286"/>
  </g>
  <text class="quote-mark" x="20" y="252">“</text>
  <text class="quote" x="20" y="258">Dan Hollis is one of the best Realtors in Colorado Springs! Thank you</text>
  <text class="quote" x="20" y="272">for the quick sale of our home and for all that you did for us!</text>
  <text class="quote-name" x="122" y="290">Marisa<tspan class="quote-role"> - CRE Client</tspan></text>
  <text class="quote-mark" x="266" y="298">”</text>

  <text class="quote-mark" x="20" y="316">“</text>
  <text class="quote" x="20" y="322">Dan is absolutely the best. Selling our home was so much easier with</text>
  <text class="quote" x="20" y="336">him as our realtor. He is always there to answer questions no matter</text>
  <text class="quote" x="20" y="350">how small. I would definitely recommend him!</text>
  <text class="quote-name" x="126" y="366">Joan Pryor</text>
  <text class="quote-role" x="116" y="378">- CRE Client - 4/13/2015</text>
  <text class="quote-mark" x="252" y="376">”</text>

  <text class="contact-lead" x="20" y="416">Get in touch with us</text>
  <rect class="fill-white" x="146" y="395" width="138" height="30"/>
  <text class="contact-phone" x="215" y="417" text-anchor="middle">482-630-9157</text>

  <text class="side-url" transform="translate(313,420) rotate(-77.5)">www.thriveatharborview.com</text>

  <g class="brand brand-small">
    <rect class="fill-olive" x="420" y="58" width="7" height="7"/>
    <text class="brand-name" x="431" y="68" font-size="19">cornerstone</text>
    <text class="brand-sub" x="535" y="81" font-size="5.5" text-anchor="end">REAL ESTATE COMPANY</text>
  </g>

  <rect class="stamp-area" x="560" y="20" width="74" height="76" fill="var(--stamp)"/>

  <g class="address-lines" stroke="var(--rule)" stroke-width="1">
    <line x1="395" y1="252" x2="626" y2="252"/>
    <line x1="395" y1="294" x2="626" y2="294"/>
    <line x1="395" y1="337" x2="626" y2="337"/>
  </g>
</svg>

</body>
</html>
```